Book Cover Design Project

Our project will culminate in a volume that will provide the first comprehensive (but non-technical) history of cyber conflict, from its pre-history, to the origins in the 1980s and up to today.

We are looking for a creative professional cover that will make this project exciting. Our existing draft is printed on 8 and 1/2 by 11 size paper, however, the final draft could be smaller or a different dimension so the background should look good even if shrunk down a bit. We'd appreciate a 300 ppi resolution at full size.

Thanks, and Good Luck!

Project Deadline Extended
Reason: We have identified our favorite designs for the book cover and are ready to commit to pay, during this stage we wanted to see if we could have a better dialogue with graphic artists to get designs closer to our favorites to give us more options. We will be posting these recommendations about what we liked and didn't on the evening of November 7 EST. Thanks for helping us on this exciting project to document cyber conflict history.

We wanted to post our thoughts on the designs submitted by November 7th.  We liked a lot of them and wanted to point out a couple of our favorites to give inspiration to anyone else who'd like the chance to participate.

Plumworks got the logo for DRRS just right, and has a nice modern conservative look

• http://www.artpitchhub.example/design/1154412/book-cover-design-by-plumsworks

VoxTilde found a great image that's striking and would draw attention to the book
• http://www.artpitchhub.example/design/1153894/book-cover-design-by-voxtilde

Teodor has done some of the most innovative designs, his recent designs for us look very professional, and we like that he's experimented with designs further afield from the original blue cover
• http://www.artpitchhub.example/design/1153637/book-cover-design-by-teodorr

Please use these works as inspiration, and keep on innovating. We've committed to paying a designer.  This work will be published and shared amongst major policy makers in DC and taught in university curriculum.  Its an exciting project, and we're glad to have design be a part of it.

Thanks,
-Owen

Target Market(s)

It will be aimed at policy makers and practitioners to give them perspective on the threats, problems and solutions of the past.

Industry/Entity Type

It Professional

Requirements
Must have
• Please design a separate background image and text overlay. The text should include the title and editor...

Title text: "A Silent Frontier: Rivalry in the Wired Age 1986 to Today"

Editor text: "Edited by Martin Delcourt"

The project is supported by both the Digital Rivalry Research Society and The Meridian Forum. These logo images are attached and should be included as part of the text overlay. I've attached our existing cover, we're looking for something new and more creative, but you can use the image for inspiration.

```html
<!DOCTYPE html>
<html lang="en">
<head>
<meta charset="utf-8">
<title>A Silent Frontier: Rivalry in the Wired Age 1986 to Today — Book Cover</title>
<link rel="stylesheet" href="https://fonts.googleapis.com/css2?family=Orbitron:wght@400;500&family=Open+Sans:wght@400&display=swap">
<style>
  :root {
    --page: #ffffff;
    --ink-deep: #06142e;
    --ink-mid: #0d3a6e;
    --ink-glow: #2f7fc4;
    --ink-teal: #0f4a4e;
    --type: #ffffff;
    --glow: rgba(140, 200, 255, 0.85);
  }
  * { margin: 0; padding: 0; box-sizing: border-box; }
  html, body {
    width: 1200px; height: 1000px; overflow: hidden;
    background: var(--page);
  }
  .cover {
    position: absolute; left: 213px; top: 0;
    width: 774px; height: 1000px; overflow: hidden;
    color: var(--type);
  }
  .cover-art {
    position: absolute; inset: 0;
    background:
      radial-gradient(ellipse 190px 260px at 50% 52%, rgba(150, 205, 255, 0.55), rgba(60, 130, 200, 0.25) 55%, transparent 75%),
      radial-gradient(ellipse 520px 420px at 50% 30%, var(--ink-glow), transparent 70%),
      linear-gradient(180deg, var(--ink-mid) 0%, #0a2c5a 45%, var(--ink-teal) 80%, var(--ink-deep) 100%);
  }
  .series {
    position: absolute; top: 36px; left: 0; right: 0;
    text-align: center;
    font: 400 20px/1 "Orbitron", sans-serif;
    letter-spacing: 0.5px;
    text-shadow: 0 0 6px var(--glow);
  }
  .title {
    position: absolute; top: 182px; left: 0; right: 0;
    text-align: center;
    text-shadow: 0 0 10px var(--glow), 0 0 22px var(--glow);
  }
  .title-line { display: block; }
  .title-tech {
    font: 400 70px/1 "Orbitron", sans-serif;
    letter-spacing: 6px;
    text-transform: uppercase;
  }
  .title-sans {
    margin: 22px 0 30px;
    font: 400 84px/1 "Open Sans", sans-serif;
  }
  .editor {
    position: absolute; top: 797px; left: 0; right: 0;
    text-align: center;
    font: 400 24px/1.5 "Orbitron", sans-serif;
    text-shadow: 0 0 6px var(--glow);
  }
  .sponsor {
    position: absolute; bottom: 32px;
    display: flex; align-items: center; gap: 12px;
    font: 400 28px/1 "Open Sans", sans-serif;
    color: var(--type);
  }
  .sponsor-mark {
    width: 52px; height: 52px; border-radius: 50%;
    background: var(--type);
  }
  .sponsor--forum { left: 24px; }
  .sponsor--society { right: 36px; font-size: 36px; }
</style>
</head>
<body>
  <main class="cover">
    <div class="cover-art" role="img" aria-label="Deep blue field of glowing binary code with a luminous fingerprint at its centre"></div>

    <p class="series">A Silent Frontier:</p>

    <h1 class="title">
      <span class="title-line title-tech">Rivalry in</span>
      <span class="title-line title-sans">the Wired Age</span>
      <span class="title-line title-tech">1986 to Today</span>
    </h1>

    <p class="editor">Edited by<br>Martin Delcourt</p>

    <div class="sponsor sponsor--forum">
      <span class="sponsor-mark"></span>
      <span class="sponsor-name">The Meridian Forum</span>
    </div>

    <div class="sponsor sponsor--society">
      <span class="sponsor-mark"></span>
      <span class="sponsor-name">DRRS</span>
    </div>
  </main>
</body>
</html>
```